Your Brimtoral App all-in-one system for transformation needs a book cover.

Hello- I would like a very similar book cover ( Under Quiet Lanterns book cover) as the sample I'm attaching. The person on my book cover would be less stiff, wear a cowboy hat, and maybe have flying hair. High-end bohemian style. Our brand colors are gold, light pink, and tan color. I'll attach App Logo and the colors we used on that. The title of my book is: "The Radiant Harvest Pathway" and I will also need formatting for ebook, audio, and paperback. Thank you, Maribel

Target Market(s)

Those who are on the path to enlightenment - 60% women 40% men

Industry/Entity Type

Consciousness Industry

Font styles to use
Other font styles liked:
• Dubai

Colors
0054AA
0677BA
7BADD7
CADEEF
E8F1F8
FFC000
F8CF3A
FAE287
FDF2CF
FEFAEE
F0912C
F2A743
F7CA91
FBE8D2
FDF5EE
EE7325
F08F49
F5BC92
FAE3D3
FDF4ED
6B429C
8869AF
B7A5CE
E3DAEB
F3F0F8

Requirements
Must have
• Light spheres - light pink, orange-pink, gold and possibly blue on the very top
Should not have
• More of a sun rise feel, less or no clouds in the upper section,

```html
<!DOCTYPE html>
<html lang="en">
<head>
<meta charset="utf-8">
<title>The Radiant Harvest Pathway – Book Cover</title>
<link rel="stylesheet" href="https://fonts.googleapis.com/css2?family=Jost:wght@500;600;700&display=swap">
<style>
  :root {
    --page-bg: #e3e3e1;
    --sky-magenta: #8f3f66;
    --sky-teal: #5cb7bd;
    --sky-orange: #ec7a3a;
    --sun-gold: #f8cf5a;
    --sun-glow: #fff6d8;
    --ground-maroon: #5a1a32;
    --ground-deep: #3f1024;
    --title-pink: #f1a2d2;
    --title-blush: #f4c6c0;
    --title-cream: #f5e0a6;
    --title-lemon: #f1ef8e;
    --author: #dcc1ba;
    --series: #e4cfc6;
  }
  * { margin: 0; padding: 0; box-sizing: border-box; }
  html, body {
    width: 1200px;
    height: 1013px;
    overflow: hidden;
    background: var(--page-bg);
  }
  .book-cover {
    position: absolute;
    left: 346px;
    top: 154px;
    width: 508px;
    height: 716px;
    overflow: hidden;
    font-family: "Jost", "Futura", sans-serif;
  }
  .cover-artwork {
    position: absolute;
    inset: 0;
    background:
      radial-gradient(ellipse 58% 22% at 52% 64%, var(--sun-glow) 0%, rgba(255,240,190,0.85) 30%, rgba(248,207,90,0) 100%),
      radial-gradient(ellipse 40% 22% at 95% 6%, var(--sky-teal) 0%, rgba(92,183,189,0) 100%),
      radial-gradient(ellipse 18% 14% at 4% 24%, var(--sky-teal) 0%, rgba(92,183,189,0) 100%),
      linear-gradient(180deg,
        var(--sky-magenta) 0%,
        #a9485a 22%,
        var(--sky-orange) 42%,
        var(--sun-gold) 58%,
        #f4a24a 70%,
        #b8433f 78%,
        var(--ground-maroon) 88%,
        var(--ground-deep) 100%);
  }
  .cover-title {
    position: absolute;
    left: 0;
    right: 0;
    top: 112px;
    text-align: center;
    padding-left: 22px;
    font-weight: 600;
    font-size: 84px;
    line-height: 79px;
    letter-spacing: 3px;
    text-transform: uppercase;
  }
  .cover-title span { display: block; }
  .cover-title .line-1 { color: var(--title-pink); margin-bottom: 18px; }
  .cover-title .line-2 { color: var(--title-blush); }
  .cover-title .line-3 { color: var(--title-cream); }
  .cover-title .line-4 { color: var(--title-lemon); }
  .cover-author {
    position: absolute;
    left: 0;
    right: 0;
    top: 580px;
    text-align: center;
    color: var(--author);
    font-weight: 600;
    font-size: 46px;
    line-height: 50px;
    letter-spacing: 5px;
    text-transform: uppercase;
  }
  .cover-author span { display: block; }
  .cover-series {
    position: absolute;
    left: 0;
    right: 0;
    top: 680px;
    text-align: center;
    color: var(--series);
    font-size: 11px;
    letter-spacing: 1.2px;
    text-transform: uppercase;
  }
  .cover-series .series-name { font-weight: 700; }
  .cover-series .series-divider { margin: 0 5px; font-weight: 500; }
  .cover-series .series-number { font-weight: 500; }
</style>
</head>
<body>
  <main class="book-cover">
    <div class="cover-artwork" role="img" aria-label="Painted sunrise landscape: a lone figure walks toward a glowing horizon across a grassy field between hills, under a warm magenta, orange and gold sky with drifting light sparks"></div>

    <h1 class="cover-title">
      <span class="line-1">The</span>
      <span class="line-2">Radiant</span>
      <span class="line-3">Harvest</span>
      <span class="line-4">Pathway</span>
    </h1>

    <p class="cover-author">
      <span>Theo</span>
      <span>Marlow</span>
    </p>

    <p class="cover-series">
      <span class="series-name">Elias Wrenfield</span><span class="series-divider">|</span><span class="series-number">Book Two</span>
    </p>
  </main>
</body>
</html>
```